Nutritional Supplement Brand in Need of a Website Cleanse!

We are in need of a website overhaul, one that will make our product, which is a healthy greens powder supplement, appear more sophisticated and appealing. Up till now most of our efforts have focused on formulating the product and setting up distribution. We did go down the internet marketing / pagetrailz selling path without too much success. What we'd like to do now is really bring focus to the benefits of the product, the ingredients, the value proposition. We would like green designs that accentuate the healthy energy and benefits the product drives (a very fresh, clean and energetic feel).
Updates

Project Deadline Extended
Reason: Extending the deadline out 5 days since I was late in providing feedback and because so many great designs were submitted. Thanks for your patience and understanding.

Target Market(s)

People who suffer from low energy levels and those who live a very active lifestyle and are in search of ways to boost their energy in a healthy way (not through coffee or sugary energy drinks). Primarily M/F in the 25-45 age range. Also people who know that they need to eat more fruits and vegetables on a daily basis but have neither the time or the money to do so.

Industry/Entity Type

Health And Wellness

Number of Pages Required

1 page

Font styles to use
Sans Serif

Colors
cadf82
acd036
b5d664
eaf2ce

Requirements
Must have
• My site is currently in Wordpress and can be seen at http://www.verdalux27blend.com
• The product can also be found on Shopvarro at https://www.shopvarro.com/dp/K47QWMZRX2
• I would like the site to remain in Wordpress and will pay extra to have the layout coded into Wordpress although this isn't a requirement for proposals.
• Here are some examples of sites around my niche that I like the look and feel of:
• http://www.plenivo.com/2-classic-cb/
• https://sprintleafusa.com/
• https://www.brisklawn.com/
• http://velaroot.com/turmeric/
• My current site is in the layout of a long-form sales letter. I don't want the new design to be so sales-pitch in manner. I want it to be more about the energy-driving benefits of the core ingredients in the formula and testimonials (designs can leverage some that are on my existing site and positive reviews on the Shopvarro listing). My current site leads with a video but this is not necessary in the redesign. I do have an edited video that's 2-3 minutes long that could be leveraged if a designer wanted to go down this path (it's absolutely not necessary though). I plan to utilize social media influencers to drive traffic to my listing so I'm hoping this will allow for a bit less sales-pitch needed on the site itself. Using all of the copy that's on the existing website in not necessary, a lot of it is redundant and it's in need of an overhaul. I'd rather slim down the site and keep it very product-focused.
• In terms of social media I'd like a link to my instagram and facebook pages:
• https://www.instagram.com/verdalux27blend/
• https://www.facebook.com/V27Blend/
• I want the site to be responsive and look great on all devices (desktop, mobile).
• I'm new to artjostle so please hit me up with further questions if needed.
Nice to have
• Would love a new look and feel to my logo. I'm not a huge fan of the current one. I can't really change the name of the product at this point but the logo on the site can be edited and a new look is encouraged.

```html
<!DOCTYPE html>
<html lang="en">
<head>
<meta charset="utf-8">
<title>Verdalux 27 Blend — Natural Energy Food</title>
<link href="https://fonts.googleapis.com/css2?family=Roboto:wght@300;400;500;700&family=Roboto+Condensed:ital,wght@0,400;0,700;1,400;1,700&display=swap" rel="stylesheet">
<style>
:root{
  --green:#8dc63f;
  --green-bright:#acd036;
  --green-soft:#b5d664;
  --green-light:#cadf82;
  --green-pale:#eaf2ce;
  --forest:#1d2a12;
  --forest-mid:#34501d;
  --ink:#2b2b2b;
  --grey:#6d6d6d;
  --wood:#ededed;
  --charcoal:#3a3a3a;
  --white:#ffffff;
}
*{box-sizing:border-box;margin:0;padding:0}
html,body{width:1200px;height:3750px;overflow:hidden}
body{position:relative;background:var(--white);font-family:"Roboto Condensed",sans-serif;color:var(--ink)}
.abs{position:absolute}
.placeholder{position:absolute}

/* hero */
.hero{position:absolute;left:0;top:0;width:1200px;height:540px;background:linear-gradient(135deg,#2c3d18 0%,#4a6a25 45%,#1a2410 100%)}
.brand{position:absolute;left:140px;top:52px;display:flex;align-items:center;gap:12px;font-family:"Roboto",sans-serif;font-weight:700;font-size:30px;color:var(--white);line-height:1}
.brand .dot{width:22px;height:22px;border-radius:50%;background:var(--green-bright)}
.nav{position:absolute;top:28px;left:466px;display:flex;align-items:center;gap:26px;font-size:13px;font-weight:700;color:var(--white);letter-spacing:.3px}
.nav .cart{background:#2a2a2a;border-radius:16px;padding:8px 18px;border:1px solid #555}
.nav .buy{background:var(--green-bright);border-radius:16px;padding:8px 20px;color:var(--forest)}
.hero-card{position:absolute;left:627px;top:235px;width:273px;height:210px;border:2px solid var(--green-bright);background:rgba(20,30,10,.35);text-align:center;padding-top:22px;color:var(--white)}
.hero-card .small{font-family:"Roboto Condensed",sans-serif;font-weight:700;font-size:40px;line-height:1}
.hero-card .big{font-family:"Roboto Condensed",sans-serif;font-weight:700;font-size:70px;line-height:.95}
.btn{display:inline-block;background:var(--green-bright);color:var(--forest);font-weight:700;font-size:14px;border-radius:4px}
.hero-card .btn{margin-top:10px;padding:10px 20px;background:#7ca824;color:var(--white)}

/* intro */
.intro-curve{position:absolute;left:0;top:460px}
.intro h1{position:absolute;left:140px;top:735px;font-family:"Roboto",sans-serif;font-weight:300;font-size:44px;line-height:1.12;color:#222}
.intro .lede{position:absolute;left:140px;top:848px;font-size:17px;color:var(--grey)}
.intro .dots{position:absolute;left:140px;top:888px;width:600px;border-top:2px dotted var(--green-soft)}
.badge{position:absolute;left:145px;top:915px;width:96px;height:96px;border-radius:50%;background:var(--green);border:4px solid var(--forest-mid);color:var(--white);font-weight:700;font-size:17px;line-height:1;display:flex;align-items:center;justify-content:center;text-align:center}
.badge-text{position:absolute;left:258px;top:938px;width:330px;font-size:21px;color:var(--green);line-height:1.2;text-transform:uppercase}

/* symptoms */
.symptoms{position:absolute;left:0;top:1090px;width:1200px;height:1232px;background:linear-gradient(180deg,#f2f2f2,#e9e9e9)}
.section-title{position:absolute;width:1200px;text-align:center;font-family:"Roboto",sans-serif;font-weight:300;font-size:44px;color:#222}
.section-title b{font-weight:500}
.symptom{position:absolute;top:1240px;width:230px;text-align:center}
.symptom .photo{width:222px;height:222px;border-radius:50%;margin:0 auto 18px;border:5px solid var(--white);box-shadow:0 2px 6px rgba(0,0,0,.25)}
.symptom h3{font-size:16px;font-weight:700;color:#222;margin-bottom:6px}
.symptom p{font-size:13px;line-height:1.3;color:var(--grey)}
.banner{position:absolute;left:145px;top:1680px;width:910px;height:145px;background:var(--green-light);text-align:center;overflow:hidden}
.banner .kicker{margin-top:26px;font-size:26px;color:var(--forest-mid)}
.banner .headline{font-family:"Roboto",sans-serif;font-weight:700;font-size:33px;color:#222;margin-top:4px}
.banner .sub{font-size:16px;color:#333;margin-top:4px}
.banner svg{position:absolute;top:0}
.share-line{position:absolute;top:1818px;width:1200px;text-align:center;font-style:italic;font-weight:700;font-size:22px;color:#222}
.col{position:absolute;font-size:15.5px;line-height:1.35;color:var(--grey)}
.tag{position:absolute;background:var(--green-bright);color:var(--forest);font-weight:700;font-size:26px;padding:8px 22px}

/* pricing */
.pricing{position:absolute;left:0;top:2322px;width:1200px;height:690px;background:linear-gradient(180deg,#333 0 200px,#4a4a4a 200px 100%)}
.guarantee-seal{position:absolute;left:296px;top:2355px;width:128px;height:128px;border-radius:50%;background:var(--forest);border:6px solid var(--green-bright)}
.guarantee{position:absolute;left:455px;top:2372px;color:var(--white);font-family:"Roboto",sans-serif;font-size:40px;line-height:1.1}
.guarantee b{font-weight:700}
.guarantee span{font-weight:300}
.plan{position:absolute;top:2580px;width:275px;height:350px;border:3px solid var(--green-bright);background:rgba(25,25,25,.55);text-align:center;color:var(--white)}
.plan .head{height:46px;background:#222;font-weight:700;font-size:24px;line-height:46px}
.plan.featured .head{background:var(--green-bright);color:var(--forest)}
.plan .name{margin-top:12px;font-size:16px;color:var(--green-bright);line-height:1.2}
.plan .jars{width:160px;height:70px;margin:16px auto 14px;background:linear-gradient(180deg,#1c1c1c,#3b5a1c);border-radius:3px}
.plan .detail{font-size:14px;line-height:1.3}
.plan .price{font-size:17px;font-weight:700;color:var(--green-bright)}
.plan .btn{margin-top:14px;padding:9px 22px;border-radius:16px;font-size:13px}
.questions{position:absolute;top:2950px;width:1200px;text-align:center;color:var(--white);font-size:20px}

/* testimonials */
.testimonial-avatar{position:absolute;left:258px;top:3245px;width:132px;height:132px;border-radius:50%;background:linear-gradient(135deg,#d9d9d9,#7a7a7a)}
.quote{position:absolute;left:420px;top:3235px;width:560px;font-style:italic;font-size:17px;line-height:1.35;color:#444}
.author{position:absolute;left:420px;top:3345px;font-weight:700;font-size:22px;color:var(--green)}
.author-role{position:absolute;left:420px;top:3378px;font-size:11.5px;color:var(--grey)}
.arrow{position:absolute;top:3290px}

/* footer */
.rule{position:absolute;left:140px;width:920px;height:2px;background:var(--green-soft)}
.foot-col{position:absolute;top:3528px;font-size:13px;font-weight:700;color:#222;line-height:1.6}
.foot-brand{position:absolute;left:528px;top:3500px;width:145px;height:145px;border-radius:50%;background:var(--forest);color:var(--white);display:flex;align-items:center;justify-content:center;text-align:center;font-family:"Roboto",sans-serif;font-weight:700;font-size:20px;line-height:1.1}
.signup{position:absolute;left:772px;top:3522px;width:285px}
.signup h4{font-size:14px;font-weight:700;margin-bottom:12px}
.signup .field{height:34px;border:2px solid var(--green-bright);font-size:11px;color:#888;padding:8px 8px}
.signup .btn{float:right;padding:6px 18px;border-radius:0;font-size:12px;color:var(--white);background:var(--green-bright)}
.copyright{position:absolute;top:3712px;width:1200px;text-align:center;font-size:12px;color:var(--grey)}
.social{position:absolute;top:3706px;width:22px;height:22px;background:#999;border-radius:3px}
</style>
</head>
<body>

<!-- HERO -->
<section class="hero" role="img" aria-label="Group of active friends celebrating outdoors in warm green light"></section>
<div class="placeholder" role="img" aria-label="Three tubs of Verdalux 27 Blend greens powder with fresh vegetables, berries and an apple" style="left:120px;top:170px;width:430px;height:410px;background:radial-gradient(ellipse at 50% 45%,#3c3c3c 0 45%,#5b7e2a 70%,rgba(90,130,40,0) 72%)"></div>
<div class="brand"><span class="dot"></span>Verdalux 27 Blend</div>
<nav class="nav">
  <span>HOME</span><span>ABOUT US</span><span>INGREDIENTS</span><span>TESTIMONIALS</span><span>PRICE</span>
  <span class="cart">CART(1)</span><span class="buy">BUY NOW</span>
</nav>
<div class="hero-card">
  <div class="small">THIS IS</div>
  <div class="big">VERDALUX<br>27 BLEND</div>
  <span class="btn">KNOW MORE</span>
</div>

<!-- INTRO -->
<svg class="intro-curve" width="1200" height="640" viewBox="0 0 1200 640" aria-hidden="true">
  <path d="M0 60 Q600 150 1200 0 L1200 640 L0 640 Z" fill="#ffffff"/>
  <path d="M0 560 L170 540 L300 575 L470 548 L640 580 L820 545 L1000 578 L1200 548 L1200 620 L0 620 Z" fill="#d6d6d6"/>
  <path d="M0 590 L200 560 L360 600 L560 565 L760 602 L960 562 L1200 598 L1200 640 L0 640 Z" fill="#acd036"/>
</svg>
<div class="placeholder" role="img" aria-label="Athletic woman in sportswear flexing and holding a tub of the supplement" style="left:735px;top:540px;width:300px;height:520px;background:radial-gradient(ellipse at 50% 45%,#c9b59a 0 30%,#9dc64a 55%,rgba(255,255,255,0) 70%)"></div>
<section class="intro">
  <h1>100% Natural Energy Food for<br>People on the Move</h1>
  <p class="lede">From now on, you don't have to settle for just a few hours of energy.</p>
  <div class="dots"></div>
  <div class="badge">ALL<br>DAY<br>ENERGY</div>
  <p class="badge-text">One new supplement does all of this and keeps you energized all day long...</p>
</section>

<!-- SYMPTOMS -->
<section class="symptoms" role="img" aria-label="Light grey wood plank texture"></section>
<h2 class="section-title" style="top:1160px">Do These Symptoms <b>Sound Familiar</b> To You?</h2>

<div class="symptom" style="left:130px">
  <div class="photo" role="img" aria-label="Stressed man holding his head" style="background:linear-gradient(135deg,#c9b8a4,#5a4a3c)"></div>
  <h3>It's difficult to stay focused</h3>
  <p>In fact, many people can't get a good night's sleep because they are loaded up with harmful ingredients like caffeine.</p>
</div>
<div class="symptom" style="left:372px">
  <div class="photo" role="img" aria-label="Tired woman yawning" style="background:linear-gradient(135deg,#e8dccb,#8a7a68)"></div>
  <h3>You get tired regularly</h3>
  <p>You just can't seem to keep your energy levels as high as you would like and get tired doing even the most mundane of tasks.</p>
</div>
<div class="symptom" style="left:614px">
  <div class="photo" role="img" aria-label="Exhausted office worker at a desk" style="background:linear-gradient(135deg,#d8d8d8,#4a5566)"></div>
  <h3>You suffer from work-fatigue</h3>
  <p>You struggle to get work done during the day and you are always reaching for more coffee or an unhealthy energy drink.</p>
</div>
<div class="symptom" style="left:843px">
  <div class="photo" role="img" aria-label="Man rubbing his temples from mental fatigue" style="background:linear-gradient(135deg,#b08868,#3a2418)"></div>
  <h3>You feel mental fatigue</h3>
  <p>The demands on you are enormous, and you often find yourself extremely tired from pressures at work or school.</p>
</div>

<div class="banner">
  <svg width="910" height="145" viewBox="0 0 910 145" aria-hidden="true" style="left:0">
    <polygon points="0,0 70,0 0,90" fill="#333"/>
    <polygon points="0,145 0,100 40,145" fill="#555"/>
    <polygon points="910,0 840,0 910,70" fill="#555"/>
    <polygon points="910,145 820,145 910,55" fill="#333"/>
  </svg>
  <div class="kicker">And here's possibly the worst part:</div>
  <div class="headline">No One Really Understands What You're Going Through.</div>
  <div class="sub">...and they might even get annoyed with you because you never seem to have enough energy.</div>
</div>

<p class="share-line">That's why what I'm going to share with you is so life changing.</p>

<div class="col" style="left:148px;top:1895px;width:250px">I'm happy to report that finally there is a natural remedy for low energy that really works. It's called...</div>
<div class="tag" style="left:130px;top:1962px">VERDALUX 27 BLEND</div>
<div class="col" style="left:148px;top:2030px;width:255px">Customers report that it works fast. It's completely guaranteed. And the price is completely reasonable. This is a major breakthrough for people suffering from low energy levels.</div>
<div class="placeholder" role="img" aria-label="Single tub of Verdalux 27 Blend greens powder" style="left:480px;top:1880px;width:250px;height:330px;background:linear-gradient(180deg,#f5f5f5 0 8%,#222 8% 80%,#e6e6e6 80%);border-radius:10px"></div>
<div class="col" style="left:765px;top:1895px;width:290px">But chances are, you've never heard of it. Because that's the way the big pharmaceutical companies want it. They spend over 30 billion dollars a year to advertise their products to the public and doctors. They have teams of sales people visiting doctors' offices daily to make sure they keep pushing their pills and prescriptions. So I understand most people haven't heard of Verdalux 27 Blend. That's the way the big drug companies want it.<br><b style="color:#222">But let me assure you,</b></div>
<div class="tag" style="left:752px;top:2172px;font-size:24px">IT WORKS!</div>

<!-- PRICING -->
<section class="pricing" role="img" aria-label="Dim photo of people training in a gym"></section>
<div class="guarantee-seal" role="img" aria-label="Money back guarantee seal"></div>
<h2 class="guarantee"><b>60 Day</b> <span>Risk Free</span><br><span>Money Back</span> <b>Guarantee</b></h2>

<div class="plan" style="left:145px">
  <div class="head">SILVER</div>
  <div class="name">Verdalux 27 Blend Single Bottle</div>
  <div class="jars" role="img" aria-label="One tub of the supplement" style="width:70px"></div>
  <div class="detail">Get One bottle of Verdalux 27 Blend</div>
  <div class="price">47.95 + FREE SHIPPING</div>
  <span class="btn">ADD TO CART</span>
</div>
<div class="plan" style="left:458px">
  <div class="head">GOLD</div>
  <div class="name">3 Month's Supply<br>of Verdalux 27 Blend</div>
  <div class="jars" role="img" aria-label="Three tubs of the supplement" style="margin-top:10px"></div>
  <div class="price" style="color:var(--white)">129.95 + FREE SHIPING</div>
  <div class="detail">43.32 per bottle</div>
  <span class="btn">ADD TO CART</span>
</div>
<div class="plan featured" style="left:772px;width:283px">
  <div class="head">PLATINUM <span style="font-size:13px;font-style:italic;font-weight:400">best value</span></div>
  <div class="name">4 Month's Supply<br>of Verdalux 27 Blend</div>
  <div class="jars" role="img" aria-label="Four tubs of the supplement" style="margin-top:10px"></div>
  <div class="price">149.95 + FREE SHIPPING</div>
  <div class="detail">Only 37.38 per bottle</div>
  <span class="btn">ADD TO CART</span>
</div>
<p class="questions">QUESTIONS? Feel free to email us at : support@verdalux27blend.com</p>

<!-- TESTIMONIALS -->
<h2 class="section-title" style="top:3060px;line-height:1.1">The Feedback Has Been<br><b>Incredible</b></h2>
<svg class="arrow" style="left:178px" width="24" height="40" viewBox="0 0 24 40" aria-hidden="true"><polyline points="20,4 4,20 20,36" fill="none" stroke="#8dc63f" stroke-width="5"/></svg>
<svg class="arrow" style="left:995px" width="24" height="40" viewBox="0 0 24 40" aria-hidden="true"><polyline points="4,4 20,20 4,36" fill="none" stroke="#8dc63f" stroke-width="5"/></svg>
<div class="testimonial-avatar" role="img" aria-label="Portrait of fitness trainer Carla Venning"></div>
<p class="quote">"I highly recommend Verdalux 27 Blend for a high quality non-GMO Superfood with vitamins, minerals, antioxidants, probiotics, and digestive enzymes. My body functions better in and out of the gym with added nutrition and it keeps my skin clear &amp; youthful, eyes bright, and energy naturally high."</p>
<p class="author">Carla Venning</p>
<p class="author-role">(Certified Nutritional Therapist, Certified Personal Trainer, Fitness Model and Regional Fitness Circuit Winner)</p>

<!-- FOOTER -->
<div class="rule" style="top:3455px"></div>
<div class="foot-col" style="left:143px">Home<br>About us<br>Ingredients<br>Testimonial</div>
<div class="foot-col" style="left:320px">Price<br>Shop Now<br>Terms &amp; conditions<br>Contact us</div>
<div class="foot-brand">Verdalux<br>27 Blend</div>
<div class="signup">
  <h4>Update for latest Offers</h4>
  <div class="field">Enter Your Email Address</div>
  <span class="btn">SUBMIT</span>
</div>
<div class="rule" style="top:3690px;height:1px;background:#ccc"></div>
<p class="copyright">2016 Verdalux 27 Blend, All Rights Reserved.</p>
<div class="social" style="left:1002px"></div>
<div class="social" style="left:1030px"></div>

</body>
</html>
```